Book Cover

Hello!
I need someone to design a book cover with the title, subtitle and one of the photos attached.

- Title: Beyond the Grey Hours - By Corwin Ashdale
- Subtitle: A Steady Handbook for finding calm and strength after hard news.

```html
<!DOCTYPE html>
<html lang="en">
<head>
<meta charset="utf-8">
<title>Beyond the Grey Hours — Book Cover</title>
<link rel="stylesheet" href="https://fonts.googleapis.com/css2?family=Oswald:wght@400;600&family=Montserrat:wght@500&display=swap">
<style>
  :root {
    --page: #ffffff;
    --cover-top: #eeedee;
    --cover-mid: #f3f3f3;
    --title-teal: #1f6b74;
    --band-blue: rgba(28, 98, 124, 0.9);
    --text-light: #ffffff;
    --photo-grey: #b9bcbd;
    --photo-dark: #4a4f52;
    --photo-teal: #1d6f6d;
    --photo-deep: #164e55;
  }
  * { margin: 0; padding: 0; box-sizing: border-box; }
  html, body {
    width: 1200px; height: 1200px; overflow: hidden;
    background: var(--page);
  }
  .book-cover {
    position: absolute; left: 200px; top: 0;
    width: 800px; height: 1200px; overflow: hidden;
    background: linear-gradient(180deg, var(--cover-top) 0%, var(--cover-mid) 45%, #f7f7f7 100%);
    box-shadow: 0 0 12px rgba(0,0,0,0.28);
  }
  .cover-photo {
    position: absolute; left: 0; top: 380px; width: 800px; height: 820px;
    background:
      radial-gradient(ellipse 38% 30% at 46% 22%, rgba(214,190,178,0.9) 0%, rgba(214,190,178,0) 100%),
      radial-gradient(ellipse 70% 55% at 55% 85%, var(--photo-teal) 0%, var(--photo-deep) 60%, rgba(22,78,85,0) 100%),
      linear-gradient(90deg, rgba(60,62,64,0.75) 0%, rgba(185,188,189,0.35) 45%, rgba(230,236,236,0.2) 100%);
    -webkit-mask-image: linear-gradient(180deg, transparent 0%, #000 18%);
            mask-image: linear-gradient(180deg, transparent 0%, #000 18%);
  }
  .cover-title {
    position: absolute; left: 0; top: 88px; width: 800px;
    text-align: center; color: var(--title-teal);
    font-family: "Oswald", sans-serif; text-transform: uppercase;
    line-height: 1;
  }
  .cover-title .title-line-one {
    display: block; font-weight: 600; font-size: 150px; letter-spacing: 1px;
  }
  .cover-title .title-line-two {
    display: block; font-weight: 400; font-size: 128px; margin-top: 22px; letter-spacing: 1px;
  }
  .subtitle-band { position: absolute; left: 0; top: 0; }
  .subtitle-text {
    position: absolute; left: 0; top: 893px; width: 800px;
    text-align: center; color: var(--text-light);
    font-family: "Montserrat", sans-serif; font-weight: 500;
    font-size: 27px; letter-spacing: 6px; line-height: 38px;
    text-transform: uppercase;
    transform: rotate(-2.9deg);
  }
  .author-name {
    position: absolute; left: 0; top: 1088px; width: 800px;
    text-align: center; color: var(--text-light);
    font-family: "Montserrat", sans-serif; font-weight: 500;
    font-size: 60px; letter-spacing: 2px; text-transform: uppercase;
  }
</style>
</head>
<body>
  <div class="book-cover">
    <div class="cover-photo" role="img" aria-label="Portrait photograph of an older grey-haired man in a teal jacket looking upward, outdoors against a soft winter background"></div>

    <h1 class="cover-title">
      <span class="title-line-one">Beyond the</span>
      <span class="title-line-two">Grey Hours</span>
    </h1>

    <svg class="subtitle-band" width="800" height="1200" viewBox="0 0 800 1200" aria-hidden="true">
      <polygon points="0,905 800,865 800,1015 0,1060" fill="var(--band-blue)"/>
    </svg>
    <p class="subtitle-text">A steady handbook<br>for finding calm and strength<br>after hard news.</p>

    <p class="author-name">Corwin Ashdale</p>
  </div>
</body>
</html>
```